KP Rubbish Removal Business Card

Hey,
I need a double sided business card designed for a rubbish removal business based in Australia. Logo is already chosen, similar colours preferred for both sides of the business card.

Details to include:

Front:

KP Rubbish Removal
Darren Holloway
Managing Director
Mobile: 0471 920 246
Email: darren@kprubbishremoval.com.au
Website: kprubbishremoval.com.au

Rear:

How did we do?
kprubbishremoval.com.au/review

```html
<!DOCTYPE html>
<html lang="en">
<head>
<meta charset="utf-8">
<title>KP Rubbish Removal – Business Card</title>
<link rel="stylesheet" href="https://fonts.googleapis.com/css2?family=Montserrat:wght@500;600;700;800&display=swap">
<style>
  :root {
    --page-bg: #eceae6;
    --card-white: #ffffff;
    --green: #1e9b3b;
    --green-dark: #127a2d;
    --green-light: #3cb54a;
    --orange: #f15a24;
    --text-white: #ffffff;
    --shadow: 0 10px 28px rgba(0, 0, 0, 0.18);
  }
  * { box-sizing: border-box; margin: 0; padding: 0; }
  html, body {
    width: 1200px; height: 900px; overflow: hidden;
    background: var(--page-bg);
    font-family: "Montserrat", sans-serif;
  }
  .canvas {
    width: 1200px; height: 900px;
    display: flex; flex-direction: column; align-items: center; justify-content: center;
    gap: 46px;
  }
  .card {
    position: relative; width: 680px; height: 390px;
    border-radius: 6px; overflow: hidden; box-shadow: var(--shadow);
  }
  /* Front */
  .card-front { background: var(--card-white); }
  .front-band { position: absolute; inset: 0; }
  .brand {
    position: absolute; top: 36px; left: 0; right: 0;
    display: flex; flex-direction: column; align-items: center; gap: 14px;
  }
  .brand-dot { width: 56px; height: 56px; border-radius: 50%; background: var(--green); }
  .brand-name {
    color: var(--green-dark); font-weight: 600; font-size: 26px; letter-spacing: 0;
  }
  .person {
    position: absolute; top: 212px; left: 0; right: 0; text-align: center; color: var(--text-white);
  }
  .person-name { font-weight: 800; font-size: 24px; letter-spacing: 1.5px; text-transform: uppercase; }
  .person-title { font-weight: 600; font-size: 14px; letter-spacing: 2px; text-transform: uppercase; margin-top: 4px; }
  .contacts {
    position: absolute; bottom: 30px; left: 28px; right: 28px;
    display: flex; justify-content: space-between; align-items: center;
    color: var(--text-white); font-weight: 500; font-size: 13.5px;
  }
  .contact { display: flex; align-items: center; gap: 7px; }
  .contact-icon {
    width: 20px; height: 20px; border-radius: 50%; background: var(--orange);
    display: flex; align-items: center; justify-content: center;
  }
  /* Back */
  .card-back {
    background: linear-gradient(135deg, var(--green-dark) 0%, var(--green) 55%, var(--green-light) 100%);
  }
  .back-pattern {
    position: absolute; inset: 0;
    background: linear-gradient(120deg, rgba(255,255,255,0) 30%, rgba(255,255,255,0.08) 100%);
  }
  .review {
    position: absolute; left: 40px; bottom: 58px;
    display: flex; align-items: center; gap: 16px;
  }
  .review-dot { width: 46px; height: 46px; border-radius: 50%; background: var(--green-light); }
  .review-question { color: var(--text-white); font-weight: 700; font-size: 19px; }
  .review-url { color: var(--orange); font-weight: 600; font-size: 27px; margin-top: 2px; }
</style>
</head>
<body>
<main class="canvas">
  <section class="card card-front" aria-label="Business card front">
    <svg class="front-band" viewBox="0 0 680 390" preserveAspectRatio="none" aria-hidden="true">
      <defs>
        <linearGradient id="bandGreen" x1="0" y1="0" x2="1" y2="1">
          <stop offset="0" stop-color="#3cb54a"/>
          <stop offset="1" stop-color="#127a2d"/>
        </linearGradient>
      </defs>
      <path d="M0 150 Q300 215 680 165 L680 390 L0 390 Z" fill="url(#bandGreen)"/>
    </svg>
    <div class="brand">
      <span class="brand-dot"></span>
      <h1 class="brand-name">KP Rubbish Removal</h1>
    </div>
    <div class="person">
      <p class="person-name">Darren Holloway</p>
      <p class="person-title">Managing Director</p>
    </div>
    <div class="contacts">
      <span class="contact">
        <span class="contact-icon"><svg width="11" height="11" viewBox="0 0 24 24"><path fill="#fff" d="M6.6 10.8a15 15 0 0 0 6.6 6.6l2.2-2.2c.3-.3.7-.4 1-.2 1.1.4 2.3.6 3.6.6.6 0 1 .4 1 1V20c0 .6-.4 1-1 1A17 17 0 0 1 3 4c0-.6.4-1 1-1h3.5c.6 0 1 .4 1 1 0 1.3.2 2.5.6 3.6.1.3 0 .7-.2 1z"/></svg></span>
        0471 920 246
      </span>
      <span class="contact">
        <span class="contact-icon"><svg width="11" height="11" viewBox="0 0 24 24"><path fill="#fff" d="M3 5h18v14H3z"/><path fill="none" stroke="#f15a24" stroke-width="2" d="M3 6l9 7 9-7"/></svg></span>
        darren@kprubbishremoval.com.au
      </span>
      <span class="contact">
        <span class="contact-icon"><svg width="11" height="11" viewBox="0 0 24 24" fill="none" stroke="#fff" stroke-width="2"><circle cx="12" cy="12" r="9"/><path d="M3 12h18M12 3c3 3 3 15 0 18M12 3c-3 3-3 15 0 18"/></svg></span>
        kprubbishremoval.com.au
      </span>
    </div>
  </section>

  <section class="card card-back" aria-label="Business card back">
    <div class="back-pattern" role="img" aria-label="Repeating brand pattern in tones of green"></div>
    <div class="review">
      <span class="review-dot"></span>
      <div>
        <p class="review-question">How did we do?</p>
        <p class="review-url">kprubbishremoval.com.au/review</p>
      </div>
    </div>
  </section>
</main>
</body>
</html>
```